Corporate Letterhead

Looking for a new corporate letterhead design. Our colors are orange and gray.

We'd like it if the below could be included somehow in the letterhead.                                       

Partnerships | Results | Quality

• Logo, Company Name, Address, Phone #, Fax #, Web address, Email address (optional), the phrase "A Service Disable Veteran Owned Small Business".

```html
<!DOCTYPE html>
<html lang="en">
<head>
<meta charset="utf-8">
<title>Vantage Systems, Inc — Letterhead</title>
<link rel="stylesheet" href="https://fonts.googleapis.com/css2?family=Source+Sans+3:wght@400;600;700&family=Exo+2:wght@700&display=swap">
<style>
  :root {
    --orange: #f0901e;
    --gray: #8a8a8a;
    --ink: #1e1e1e;
    --rule: #c8c8c8;
    --paper: #ffffff;
    --backdrop: #e9e7e4;
    --watermark: #fdf1e2;
  }
  * { margin: 0; padding: 0; box-sizing: border-box; }
  html, body {
    width: 931px; height: 1200px; overflow: hidden;
    background: var(--backdrop);
  }
  .letterhead {
    position: absolute; left: 76px; top: 43px;
    width: 787px; height: 1112px;
    background: var(--paper);
    font-family: "Source Sans 3", sans-serif;
    color: var(--ink);
    box-shadow: 0 2px 10px rgba(0,0,0,0.12);
  }
  .brand {
    position: absolute; left: 192px; top: 40px;
    display: flex; align-items: center; gap: 12px;
  }
  .brand-dot {
    width: 54px; height: 54px; border-radius: 50%;
    background: var(--orange);
  }
  .brand-name {
    font-weight: 700; font-size: 30px; line-height: 1;
    color: var(--orange); letter-spacing: 0.5px;
  }
  .values {
    position: absolute; left: 294px; top: 104px;
    font-weight: 700; font-size: 13px; color: var(--gray);
  }
  .values .accent { color: var(--orange); }
  .divider {
    position: absolute; left: 594px; top: 50px;
    width: 1px; height: 56px; background: var(--rule);
  }
  .address {
    position: absolute; left: 607px; top: 52px;
    font-size: 13.5px; line-height: 17px; font-style: normal;
  }
  .watermark {
    position: absolute; left: 228px; top: 344px;
    width: 340px; height: 340px; border-radius: 50%;
    background: var(--watermark);
  }
  .contacts {
    position: absolute; left: 0; right: 0; top: 1049px;
    display: flex; justify-content: center; align-items: center; gap: 7px;
    font-size: 13.5px;
  }
  .contacts .item { display: flex; align-items: center; gap: 4px; }
  .contacts svg { width: 12px; height: 12px; fill: var(--ink); }
  .designation {
    position: absolute; left: 0; right: 0; top: 1079px;
    text-align: center;
    font-family: "Exo 2", sans-serif; font-weight: 700;
    font-size: 12px; letter-spacing: 1.3px; color: var(--orange);
  }
</style>
</head>
<body>
  <main class="letterhead">
    <header>
      <div class="brand">
        <span class="brand-dot"></span>
        <span class="brand-name">VANTAGE SYSTEMS, INC</span>
      </div>
      <p class="values">Partnerships | <span class="accent">Results</span> | Quality</p>
      <span class="divider"></span>
      <address class="address">
        4120 Commerce Drive<br>
        Suite 210<br>
        Linthicum, MD 21090
      </address>
    </header>

    <div class="watermark" aria-hidden="true"></div>

    <footer>
      <div class="contacts">
        <span class="item">
          <svg viewBox="0 0 24 24"><path d="M6.6 10.8a15 15 0 0 0 6.6 6.6l2.2-2.2c.3-.3.7-.4 1-.2 1.1.4 2.3.6 3.6.6.6 0 1 .4 1 1V20c0 .6-.4 1-1 1A17 17 0 0 1 3 4c0-.6.4-1 1-1h3.5c.6 0 1 .4 1 1 0 1.3.2 2.5.6 3.6.1.3 0 .7-.2 1z"/></svg>
          443-555-0142
        </span>
        <span class="item">
          <svg viewBox="0 0 24 24"><path d="M6 2h12v6H6zM3 9h18a1 1 0 0 1 1 1v7h-4v5H6v-5H2v-7a1 1 0 0 1 1-1zm5 7v4h8v-4z"/></svg>
          410-555-0187
        </span>
        <span class="item">
          <svg viewBox="0 0 24 24"><path d="M2 5h20v14H2zm2 2v.5l8 5 8-5V7zm0 3v7h16v-7l-8 5z"/></svg>
          info@vantagesysinc.com
        </span>
        <span class="item">
          <svg viewBox="0 0 24 24"><path d="M12 2a10 10 0 1 0 0 20 10 10 0 0 0 0-20zm7.9 9h-3.9a15 15 0 0 0-1.4-6.3A8 8 0 0 1 19.9 11zM12 4c.9 1.2 1.8 3.7 2 7h-4c.2-3.3 1.1-5.8 2-7zM9.4 4.7A15 15 0 0 0 8 11H4.1a8 8 0 0 1 5.3-6.3zM4.1 13H8a15 15 0 0 0 1.4 6.3A8 8 0 0 1 4.1 13zM12 20c-.9-1.2-1.8-3.7-2-7h4c-.2 3.3-1.1 5.8-2 7zm2.6-.7A15 15 0 0 0 16 13h3.9a8 8 0 0 1-5.3 6.3z"/></svg>
          www.vantagesysinc.com
        </span>
      </div>
      <p class="designation">A Service Disable Veteran Owned Small Business</p>
    </footer>
  </main>
</body>
</html>
```